I need beautiful business cards with Sparrows and tulips on then and my linkwall business name is Sparrows and tulips.
I sell mini gardens, candles and melts and gift ware....on the other side I would like some thing like...REMEMBER to keep in touch with Sparrows and tulips buy a like,comment or just to say hello or link wall will think you are no longer interested and delete you....you can change the wording to that to make smaller if you would like, and am not sure how to word it....my color theme for my business in purple and green. thank you.

Industry/Entity Type

Business

Contact Information for Business Card

link wall:Sparrows and tulips
mini gardens
candles and melts
gift ware.
email:rosie814@kelpnet.com
phone:0857314026

```html
<!DOCTYPE html>
<html lang="en">
<head>
<meta charset="utf-8">
<title>Sparrows and tulips – business card</title>
<link rel="stylesheet" href="https://fonts.googleapis.com/css2?family=Cinzel:wght@500&family=Alegreya:ital,wght@1,500&family=Open+Sans:wght@400;500&display=swap">
<style>
  :root {
    --page-bg: #f4f4f6;
    --card-front-bg: #eee8f3;
    --pattern-tone: #ddd0e8;
    --brand-green: #6fbf3c;
    --brand-purple: #6b2e8f;
    --band-purple: #8a4aa6;
    --back-top: #9550ad;
    --back-bottom: #5f2a8a;
    --silhouette: rgba(120, 60, 160, 0.55);
    --text-light: #ffffff;
  }
  * { box-sizing: border-box; margin: 0; padding: 0; }
  html, body {
    width: 1200px; height: 900px; overflow: hidden;
    background: var(--page-bg);
  }
  .sheet {
    position: relative; width: 1200px; height: 900px;
    display: flex; align-items: center; justify-content: center; gap: 50px;
  }
  .card {
    position: relative; width: 540px; height: 310px;
    border-radius: 26px; overflow: hidden;
    box-shadow: 0 14px 30px rgba(0,0,0,0.12);
  }

  /* Front */
  .card-front { background: var(--card-front-bg); }
  .front-pattern {
    position: absolute; inset: 0;
    background: radial-gradient(ellipse at 70% 40%, var(--pattern-tone), transparent 70%),
                radial-gradient(ellipse at 20% 80%, var(--pattern-tone), transparent 60%);
    opacity: 0.8;
  }
  .brand {
    position: absolute; left: 22px; top: 34px;
    display: flex; align-items: flex-end; gap: 10px;
  }
  .brand-name {
    font-family: "Cinzel", serif; font-weight: 500;
    font-size: 38px; line-height: 40px; color: var(--brand-green);
    white-space: nowrap;
  }
  .brand-line { display: block; }
  .brand-dot {
    width: 16px; height: 16px; border-radius: 50%;
    background: var(--brand-green);
    margin-bottom: 12px;
  }
  .tagline {
    position: absolute; left: 24px; top: 126px;
    font-family: "Alegreya", serif; font-style: italic; font-weight: 500;
    font-size: 22px; line-height: 26px; color: var(--brand-purple);
    white-space: nowrap;
  }
  .contact {
    position: absolute; left: 22px; top: 212px;
    list-style: none;
    font-family: "Open Sans", sans-serif; font-size: 19px;
    color: var(--brand-purple); line-height: 32px;
  }
  .contact li { display: flex; align-items: center; gap: 6px; }
  .contact svg { width: 18px; height: 18px; fill: var(--brand-green); }
  .front-band {
    position: absolute; left: 0; right: 0; bottom: 0; height: 26px;
    background: var(--band-purple);
    border-top: 4px solid var(--brand-green);
  }

  /* Back */
  .card-back {
    background: linear-gradient(180deg, var(--back-top), var(--back-bottom));
  }
  .back-deco-top {
    position: absolute; left: 20px; top: 14px; width: 120px; height: 110px;
    border-radius: 50%;
    background: radial-gradient(circle, var(--silhouette), transparent 70%);
  }
  .back-deco-bottom {
    position: absolute; right: 40px; bottom: 40px; width: 140px; height: 120px;
    border-radius: 50%;
    background: radial-gradient(circle, rgba(190,140,220,0.45), transparent 70%);
  }
  .reminder {
    position: absolute; left: 0; right: 0; top: 82px;
    text-align: center;
    font-family: "Open Sans", sans-serif; font-size: 18px; line-height: 27px;
    color: var(--text-light);
  }
  .reminder .reminder-brand {
    display: block;
    font-family: "Cinzel", serif; font-weight: 500;
    font-size: 19px; color: var(--brand-green);
  }
</style>
</head>
<body>
<main class="sheet">
  <section class="card card-front" aria-label="Card front">
    <div class="front-pattern" role="img" aria-label="Soft lavender floral damask pattern"></div>
    <div class="brand">
      <span class="brand-name">
        <span class="brand-line">Sparrows</span>
        <span class="brand-line">and Tulips</span>
      </span>
      <span class="brand-dot"></span>
    </div>
    <p class="tagline">mini gardens candles and melts gift ware</p>
    <ul class="contact">
      <li>
        <svg viewBox="0 0 24 24" aria-hidden="true"><path d="M6.6 10.8a15.1 15.1 0 0 0 6.6 6.6l2.2-2.2a1 1 0 0 1 1-.25 11.4 11.4 0 0 0 3.6.57 1 1 0 0 1 1 1V20a1 1 0 0 1-1 1A17 17 0 0 1 3 4a1 1 0 0 1 1-1h3.5a1 1 0 0 1 1 1c0 1.25.2 2.450.57 3.57a1 1 0 0 1-.25 1z"/></svg>
        0857314026
      </li>
      <li>
        <svg viewBox="0 0 24 24" aria-hidden="true"><path d="M3 5h18a1 1 0 0 1 1 1v12a1 1 0 0 1-1 1H3a1 1 0 0 1-1-1V6a1 1 0 0 1 1-1zm9 7.5L20 7H4z"/></svg>
        rosie814@kelpnet.com
      </li>
    </ul>
    <div class="front-band"></div>
  </section>

  <section class="card card-back" aria-label="Card back">
    <div class="back-deco-top" role="img" aria-label="Faint insect silhouettes"></div>
    <div class="back-deco-bottom" role="img" aria-label="Faint winged silhouettes"></div>
    <p class="reminder">
      REMEMBER to keep in touch with
      <span class="reminder-brand">Sparrows and Tulips</span>
      buy a like,comment or just to say hello or<br>
      link wall will think you are no longer interested<br>
      and delete you....
    </p>
  </section>
</main>
</body>
</html>
```